We need logo design and homepage fora new company based in Estonia called "Tallow Crest Supply". We sell railway parts.

Page should look a little like www.corvintal-brask.com

Target market is Estonia and railway builders in Baltic States.

Preferred colour combination may be brown/white.

We need more pages: Company profile/ Productcs / About US

Maybe you can add random railway pictures.

Texts and other pictures we will add later, we dont have any of them right now.

Target Market(s)

Logo Text

Tallow Crest Supply

Number of Pages Required

3 page

Font styles to use
Sans Serif

Colors

Designer to choose colors to be used in the design.

Requirements
Must have
• Must have a proper and elegant start page

```html
<!DOCTYPE html>
<html lang="en">
<head>
<meta charset="utf-8">
<title>Tallow Crest Supply</title>
<link rel="stylesheet" href="https://fonts.googleapis.com/css2?family=Nunito+Sans:wght@400;600;700;800;900&display=swap">
<style>
:root{
  --brown:#4e2b17;
  --brown-deep:#3d2112;
  --brown-band:#5e3c2a;
  --ink:#3a3a3a;
  --muted:#6d6d6d;
  --line:#d8d8d8;
  --light:#f7f7f7;
  --dark:#1b1b1b;
  --white:#ffffff;
}
*{box-sizing:border-box;margin:0;padding:0}
html,body{width:1200px;height:3947px;overflow:hidden}
body{font-family:"Nunito Sans",Arial,sans-serif;color:var(--ink);background:var(--white);position:relative}
.section{position:absolute;left:0;width:1200px}
.center{text-align:center}

/* header */
.site-header{top:0;height:145px;background:var(--white)}
.brand{position:absolute;left:92px;top:22px;width:210px;text-align:center;color:var(--brown-deep)}
.brand-mark{display:block;width:46px;height:46px;border-radius:50%;background:var(--brown);margin:0 auto 8px}
.brand-name{font-size:24px;font-weight:800;letter-spacing:.5px;line-height:1.05}
.brand-sub{font-size:15px;font-weight:800;letter-spacing:1px}
.main-nav a{position:absolute;top:66px;font-size:15px;font-weight:600;color:#333;text-decoration:none;letter-spacing:.5px}
.main-nav a.active{color:var(--brown)}
.main-nav a.active::after{content:"";position:absolute;left:0;right:0;bottom:-10px;height:2px;background:var(--brown)}

/* hero */
.hero{top:145px;height:645px;background:linear-gradient(180deg,#2c3440 0%,#3b4450 45%,#4a4c50 75%,#2a2c30 100%)}
.hero-title{position:absolute;top:165px;width:100%;font-size:70px;font-weight:800;color:var(--white);letter-spacing:1.5px}
.hero-text{position:absolute;top:250px;left:200px;width:800px;font-size:19px;line-height:1.5;color:#f0f0f0}
.hero-btn{position:absolute;top:342px;left:508px;width:189px;height:47px;background:var(--brown-deep);color:var(--white);font-size:18px;font-weight:700;line-height:47px;letter-spacing:.5px}
.hero-dots{position:absolute;top:542px;left:570px;display:flex;gap:4px}
.hero-dots span{width:16px;height:16px;border-radius:50%;background:var(--white)}
.hero-dots span:first-child{background:transparent;border:2px solid var(--white)}
.hero-curve{position:absolute;left:0;bottom:0}

/* welcome */
.welcome{top:790px;height:510px}
.h2{font-size:38px;font-weight:800;letter-spacing:1px}
.welcome .h2{margin-top:44px;color:var(--brown-deep)}
.body-text{font-size:14.5px;line-height:1.6;color:var(--muted);width:930px;margin:0 auto}
.welcome .p1{margin-top:34px}
.welcome .p2{margin-top:22px}
.outline-btn{display:block;width:194px;height:51px;border:2px solid #bdbdbd;margin:56px auto 0;line-height:47px;font-size:18px;font-weight:700;color:var(--brown-deep)}

/* band */
.band{top:1300px;height:498px;background:linear-gradient(180deg,#6a4632 0%,#5a3826 50%,#4b2d1e 100%);color:var(--white)}
.band .h2{margin-top:112px;font-size:58px}
.band p{width:935px;margin:28px auto 0;font-size:19px;line-height:1.55}

/* products */
.products{top:1798px;height:623px}
.products .h2{margin-top:76px;color:#333}
.product{position:absolute;top:168px;width:200px;text-align:center}
.product-photo{width:158px;height:158px;border-radius:50%;border:6px solid var(--brown-deep);margin:0 auto}
.product-name{margin-top:18px;font-size:20px;font-weight:800;color:#2e2e2e}
.product-desc{margin-top:6px;font-size:11px;line-height:1.5;color:var(--muted);padding:0 14px}
.solid-btn{position:absolute;top:497px;left:508px;width:184px;height:47px;background:var(--brown-deep);color:var(--white);font-size:18px;font-weight:700;line-height:47px}

/* video */
.video{top:2421px;height:806px;background:var(--light)}
.video .h2{margin-top:72px;color:#333}
.video .intro{width:960px;margin:20px auto 0;font-size:16px;line-height:1.6;color:#555}
.video-frame{position:absolute;top:263px;left:97px;width:1003px;height:435px;background:var(--white);border:1px solid #e6e6e6;padding:13px}
.video-still{position:relative;width:100%;height:100%;background:linear-gradient(110deg,#d4a05a 0%,#b88a5a 25%,#7a6a62 50%,#8f8c92 70%,#4a4a52 100%)}
.play{position:absolute;left:446px;top:160px}

/* contact */
.contact{top:3227px;height:629px;background:var(--dark);color:var(--white)}
.contact .h2{margin-top:100px}
.contact .sub{margin-top:14px;font-size:14px;color:#cfcfcf}
.field{position:absolute;background:var(--white);color:#9a9a9a;font-size:13px;padding:0 12px;line-height:45px;height:45px;top:252px}
.field.message{top:318px;left:100px;width:1000px;height:74px;line-height:36px}
.submit{position:absolute;top:426px;left:495px;width:210px;height:53px;background:var(--brown-deep);color:var(--white);font-size:18px;font-weight:700;line-height:53px;letter-spacing:.5px}

/* footer */
.site-footer{top:3856px;height:91px;background:var(--white)}
.site-footer p{margin-top:36px;font-size:13px;color:#555}
</style>
</head>
<body>

<header class="section site-header">
  <div class="brand">
    <span class="brand-mark"></span>
    <div class="brand-name">TALLOW CREST</div>
    <div class="brand-sub">SUPPLY</div>
  </div>
  <nav class="main-nav">
    <a class="active" href="#" style="left:497px">HOME</a>
    <a href="#" style="left:604px">PROFILE</a>
    <a href="#" style="left:726px">PRODUCTS</a>
    <a href="#" style="left:867px">ABOUT US</a>
    <a href="#" style="left:1003px">CONTACT US</a>
  </nav>
</header>

<section class="section hero center" role="img" aria-label="Railway station platform with a passing train">
  <h1 class="hero-title">TALLOW CREST SUPPLY</h1>
  <p class="hero-text">Duis aute irure dolor in reprehenderit in voluptate velit esse cillum dolore eu fugiat nulla pariatur. Excepteur sint occaecat cupidatat non proident.</p>
  <div class="hero-btn">GET IN TOUCH</div>
  <div class="hero-dots"><span></span><span></span><span></span></div>
  <svg class="hero-curve" width="1200" height="80" viewBox="0 0 1200 80"><path d="M0 20 Q600 110 1200 20 L1200 80 L0 80 Z" fill="#ffffff"/></svg>
</section>

<section class="section welcome center">
  <h2 class="h2">WELCOME TO TALLOW CREST SUPPLY</h2>
  <p class="body-text p1">Lorem ipsum dolor sit amet, consectetur adipiscing elit, sed do eiusmod tempor incididunt ut labore et dolore magna aliqua. Ut enim ad minim veniam, quis nostrud exercitation ullamco laboris nisi ut aliquip ex ea commodo consequat. Duis aute irure dolor in reprehenderit in voluptate velit esse cillum dolore eu fugiat nulla pariatur. Excepteur sint occaecat cupidatat non proident, sunt in culpa qui officia deserunt mollit anim id est laborum.</p>
  <p class="body-text p2">Sed ut perspiciatis unde omnis iste natus error sit voluptatem accusantium doloremque laudantium, totam rem aperiam, eaque ipsa quae ab illo inventore veritatis et quasi architecto beatae vitae dicta sunt explicabo. Nemo enim ipsam voluptatem quia voluptas sit aspernatur aut odit aut fugit, sed quia consequuntur magni dolores eos qui ratione voluptatem sequi nesciunt.</p>
  <div class="outline-btn">READ MORE</div>
</section>

<section class="section band center" role="img" aria-label="Rail yard with tank wagons in brown tones">
  <h2 class="h2">WE SELL RAILWAY PARTS</h2>
  <p>But I must explain to you how all this mistaken idea of denouncing pleasure and praising pain was born and I will give you a complete account of the system, and expound the actual teachings of the great explorer of the truth, the master-builder of human happiness. No one rejects, dislikes, or avoids pleasure itself, because it is pleasure, but because those who do not know how to pursue pleasure rationally encounter consequences that are extremely painful.</p>
</section>

<section class="section products center">
  <h2 class="h2">OUR PRODUCTS</h2>
  <div class="product" style="left:82px">
    <div class="product-photo" role="img" aria-label="Close-up of a railway wheel" style="background:radial-gradient(circle,#7a5a3e,#3a2618)"></div>
    <div class="product-name">Mollitia Animi</div>
    <p class="product-desc">Lorem ipsum dolor sit amet, consectetur adipiscing elit, sed do eiusmod tempor incididunt ut labore et dolore magna.</p>
  </div>
  <div class="product" style="left:292px">
    <div class="product-photo" role="img" aria-label="Yellow rail maintenance machinery" style="background:radial-gradient(circle,#c9b24a,#5d6470)"></div>
    <div class="product-name">Earum Rerum</div>
    <p class="product-desc">Lorem ipsum dolor sit amet, consectetur adipiscing elit, sed do eiusmod tempor incididunt ut labore et dolore magna.</p>
  </div>
  <div class="product" style="left:500px">
    <div class="product-photo" role="img" aria-label="Wagon bogie and suspension" style="background:radial-gradient(circle,#8a7a6e,#3b3432)"></div>
    <div class="product-name">Cumque Nihil</div>
    <p class="product-desc">Lorem ipsum dolor sit amet, consectetur adipiscing elit, sed do eiusmod tempor incididunt ut labore et dolore magna.</p>
  </div>
  <div class="product" style="left:708px">
    <div class="product-photo" role="img" aria-label="Rusty freight wagons under a blue sky" style="background:linear-gradient(180deg,#7fa0c0,#a65a34)"></div>
    <div class="product-name">Quidem Rerum</div>
    <p class="product-desc">Lorem ipsum dolor sit amet, consectetur adipiscing elit, sed do eiusmod tempor incididunt ut labore et dolore magna.</p>
  </div>
  <div class="product" style="left:921px">
    <div class="product-photo" role="img" aria-label="Red steam locomotive wheels" style="background:radial-gradient(circle,#b23a30,#2a2a2a)"></div>
    <div class="product-name">Ducimus Qui</div>
    <p class="product-desc">Lorem ipsum dolor sit amet, consectetur adipiscing elit, sed do eiusmod tempor incididunt ut labore et dolore magna.</p>
  </div>
  <div class="solid-btn">VIEW MORE</div>
</section>

<section class="section video center">
  <h2 class="h2">OUR VIDEO</h2>
  <p class="intro">At vero eos et accusamus et iusto odio dignissimos ducimus qui blanditiis praesentium voluptatum deleniti atque corrupti quos dolores et quas molestias excepturi sint occaecati cupiditate non provident.</p>
  <div class="video-frame">
    <div class="video-still" role="img" aria-label="Railway track at sunset with a fast train passing">
      <svg class="play" width="90" height="90" viewBox="0 0 90 90"><circle cx="45" cy="45" r="41" fill="rgba(255,255,255,.15)" stroke="#ffffff" stroke-width="5" opacity=".8"/><path d="M36 28 L63 45 L36 62 Z" fill="#ffffff" opacity=".85"/></svg>
    </div>
  </div>
</section>

<section class="section contact center">
  <h2 class="h2">CONTACT US</h2>
  <p class="sub">Contact us at the following for and General Enquiries</p>
  <div class="field" style="left:100px;width:237px;text-align:left">First name</div>
  <div class="field" style="left:355px;width:235px;text-align:left">Last name</div>
  <div class="field" style="left:608px;width:237px;text-align:left">Email address</div>
  <div class="field" style="left:863px;width:237px;text-align:left">Phone number</div>
  <div class="field message" style="text-align:left">Message</div>
  <div class="submit">SUBMIT NOW !</div>
</section>

<footer class="section site-footer center">
  <p>© 2017 TALLOW CREST SUPPLY. All right reserved. Term of Use</p>
</footer>

</body>
</html>
```